Weight gainer supplement design

Looking for a design for a weight gainer /meal replacement supplement. The black plastic tub we will use has 2 spaces for sticker one around the rim approx 2.8cm tall x 30cm wideAnother around the main tub. The main sticker size will be 18cm tall by 70cm this will include the front of the product then wrap around to show the nutritional table.The brand is KTV (Kestrel training vitals) and the product will be called ALPHA MASSThe target ordience is men aged 16-35 its should have a profesional feel to it. The product comes in a black tub, the colores we would like to use are black and blue or red or gold or silver but we are open to suggestions and would like artistic imput. Are logo for KTV is attached but can be changed if the designer prefers.Attached is 1. KTV logo2. Image of similar product that comes in the same tub3 - 5 - images of similar products that we like the design of.The product is 12lbs and will be vanilla flavor. Please ask for more suggestions if needed, I have kept this description short to try and get artistic input.Thanks in advance :)
Updates

Target Market(s)

18-35 males who go to the gym

Industry/Entity Type

Fitness

Colors

Designer to choose colors to be used in the design.

Requirements
Must have
• name bravo bulk, logo KTV
Should not have
• images of people

```html
<!DOCTYPE html>
<html lang="en">
<head>
<meta charset="utf-8">
<title>KTV Bravo Bulk – Tub Label</title>
<link href="https://fonts.googleapis.com/css2?family=Russo+One&family=Oswald:wght@500;600;700&family=Archivo+Narrow:wght@400;700&display=swap" rel="stylesheet">
<style>
  :root {
    --ink: #07090c;
    --mesh: #14181e;
    --blue: #1f74c4;
    --blue-deep: #124a86;
    --white: #ffffff;
    --grey: #8a9099;
    --panel-ink: #000000;
  }
  * { margin: 0; padding: 0; box-sizing: border-box; }
  html, body { width: 1200px; height: 333px; overflow: hidden; background: var(--white); }
  .label {
    position: relative; width: 1200px; height: 333px; overflow: hidden;
    background: var(--ink);
  }
  .mesh-bg {
    position: absolute; inset: 0;
    background: radial-gradient(ellipse at 60% 50%, var(--mesh) 0%, var(--ink) 75%);
  }
  .art { position: absolute; inset: 0; }
  .side-copy {
    position: absolute; left: 4px; top: 4px; width: 135px; height: 325px;
    display: flex; gap: 3px;
  }
  .side-copy p {
    writing-mode: vertical-rl; transform: rotate(180deg);
    font: 400 6.5px/8px "Archivo Narrow", sans-serif; color: var(--grey);
    width: 16px; overflow: hidden; white-space: nowrap;
  }
  .brand-name {
    position: absolute; left: 500px; top: 50px; width: 130px; text-align: center;
    font: 400 50px/1 "Russo One", sans-serif; color: var(--white); letter-spacing: 2px;
  }
  .tagline {
    position: absolute; left: 422px; top: 127px;
    font: 600 17px/1 "Oswald", sans-serif; color: var(--ink); letter-spacing: .2px;
  }
  .product-name {
    position: absolute; left: 300px; top: 150px;
    font: 400 50px/1 "Russo One", sans-serif; color: var(--white); letter-spacing: 4px;
  }
  .servings { position: absolute; left: 652px; top: 222px; display: flex; align-items: flex-start; }
  .servings-count { font: 400 46px/1 "Russo One", sans-serif; color: var(--white); }
  .servings-word {
    writing-mode: vertical-rl; font: 600 10px/1 "Oswald", sans-serif; color: var(--white);
    margin-left: 3px; letter-spacing: .5px;
  }
  .net-weight { position: absolute; left: 388px; top: 260px; color: var(--white); }
  .net-weight h3 { font: 500 15px/1.05 "Oswald", sans-serif; }
  .net-weight p { font: 700 10.5px/1.15 "Oswald", sans-serif; }
  .macros {
    position: absolute; left: 840px; top: 14px; width: 60px; height: 134px;
    background: var(--blue); display: flex; flex-direction: column;
  }
  .macros span {
    flex: 1; display: flex; align-items: center; justify-content: center;
    font: 500 19px/1 "Oswald", sans-serif; color: var(--white);
    border-bottom: 2px solid var(--white);
  }
  .macros span:last-child { border-bottom: 0; }
  .macro-rule { position: absolute; left: 886px; top: 148px; width: 2px; height: 175px; background: var(--white); }
  .facts {
    position: absolute; left: 964px; top: 27px; width: 202px; height: 274px;
    background: var(--white); border: 1px solid var(--panel-ink); padding: 3px 5px;
    font: 400 7.2px/1.25 Arial, Helvetica, sans-serif; color: var(--panel-ink);
  }
  .facts h2 { font: 900 20px/1 "Archivo Narrow", Arial, sans-serif; border-bottom: 1px solid; padding-bottom: 1px; }
  .facts .thick { border-bottom: 5px solid var(--panel-ink); padding-bottom: 2px; }
  .facts .mid { border-bottom: 2.5px solid var(--panel-ink); }
  .row { display: flex; justify-content: space-between; border-bottom: 1px solid var(--panel-ink); padding: .6px 0; }
  .row.sub { padding-left: 10px; }
  .row b { font-weight: 700; }
  .small { font-size: 5.5px; }
  .right { text-align: right; }
  .ingredients { margin-top: 4px; text-align: justify; line-height: 1.3; }
  .contains { margin-top: 4px; }
</style>
</head>
<body>
<div class="label">
  <div class="mesh-bg" role="img" aria-label="Dark hexagon mesh pattern"></div>

  <div class="side-copy">
    <p>Directions: mix one scoop with water or milk.</p>
    <p>Shake well and drink after your training.</p>
    <p>Store in a cool dry place away from sun.</p>
    <p>Keep out of reach of young children.</p>
    <p>Not a sole source of daily nutrition.</p>
    <p>Use with a balanced diet and exercise.</p>
    <p>Made in a facility that handles nuts.</p>
  </div>

  <svg class="art" width="1200" height="333" viewBox="0 0 1200 333">
    <defs>
      <radialGradient id="clawTone" cx="45%" cy="50%" r="60%">
        <stop offset="0" stop-color="#2a86d8"/>
        <stop offset="1" stop-color="#0d2f55"/>
      </radialGradient>
    </defs>
    <polygon class="torn-field" fill="var(--blue)"
      points="240,32 300,48 335,60 380,30 420,22 470,30 520,24 570,34 610,30 650,44 700,52 740,40 765,44 770,92 790,140 768,182 760,206 772,250 735,262 690,272 640,288 600,302 560,282 540,284 500,300 480,298 440,272 410,286 360,300 330,280 300,258 260,236 220,214 196,196 182,150 214,124 200,86 222,56"/>
    <path role="img" aria-label="Claw scratch illustration"
      fill="url(#clawTone)" opacity=".9"
      d="M188,40 C240,30 300,70 380,110 C410,125 420,150 400,170 C370,200 320,215 270,210 C230,205 200,190 190,160 C180,120 175,70 188,40 Z"/>
  </svg>

  <div class="brand-name">KTV</div>
  <div class="tagline">WEIGHT GAINER/ MEAL REPLACEMENT SUPPLEMENT</div>
  <h1 class="product-name">BRAVO BULK</h1>
  <div class="servings">
    <span class="servings-count">20</span>
    <span class="servings-word">SERVINGS</span>
  </div>
  <div class="net-weight">
    <h3>NT WEIGHT 20.2</h3>
    <p>LOREM IPSUM DOLOR SIT AMET, CON</p>
    <p>LOREM IPSUM DOLOR SIT AMET, CON</p>
  </div>

  <div class="macros"><span>30 P</span><span>20 C</span><span>2 F</span></div>
  <div class="macro-rule"></div>

  <section class="facts">
    <h2>Nutrition Facts</h2>
    <div class="thick">Serving Size 1 scoop (30g)<br>Servings Per Container 30</div>
    <div class="small" style="border-bottom:1px solid;font-weight:700">Amount Per Serving</div>
    <div class="row mid"><span><b>Calories</b> 110</span><span>Calories from Fat 5</span></div>
    <div class="small right" style="border-bottom:1px solid;font-weight:700">% Daily Value*</div>
    <div class="row"><span><b>Total Fat</b> 1g</span><b>2%</b></div>
    <div class="row sub"><span>Saturated Fat 0g</span><b>0%</b></div>
    <div class="row sub"><span>Trans Fat 0g</span><span></span></div>
    <div class="row"><span><b>Cholesterol</b> 15mg</span><b>5%</b></div>
    <div class="row"><span><b>Potassium</b> 110mg</span><b>4%</b></div>
    <div class="row"><span><b>Sodium</b> 190mg</span><b>8%</b></div>
    <div class="row"><span><b>Total Carbohydrate</b> 2g</span><b>1%</b></div>
    <div class="row sub"><span>Dietary Fiber 1g</span><b>4%</b></div>
    <div class="row sub"><span>Sugars &lt;1g</span><span></span></div>
    <div class="row mid"><span><b>Protein</b> 23g</span><b>46%</b></div>
    <p class="ingredients"><b>Ingredients</b> Protein Blend (Whey Protein Isolate, Micellar Casein, Milk Protein Isolate) Peanuts, Natural Flavors. <b>Contains less than 2% of the following:</b> Sunflower Lecithin, Xanthan Gum, Cellulose Gum, Stevia Glycosides (Stevia), Salt, Sucralose</p>
    <p class="contains"><b>Contains</b> Milk Derived Ingredients, Peanuts</p>
  </section>
</div>
</body>
</html>
```